Consulting Company needs business card design

We need a business card design for a new consulting and business solutions company based in Bermuda called Corvane Holdings Limited. Looking for a double sided business card with one side only including the company logo thats attached and the other including contact information. Logo contains blue and turquoise colors and is fine to be on both sides of the card.
Contact Information for Business Card
Corvane Holdings Limited
P.O. Box KR318
Pemberly KR LT
Bermuda
Name: Marcus Telford
Position: Director
Telephone: 1 441 732 4590
Email: mtelford@corvane.bm
Website: www.corvane.bm

```html
<!DOCTYPE html>
<html lang="en">
<head>
<meta charset="utf-8">
<title>Corvane Holdings Limited — Business Card</title>
<link href="https://fonts.googleapis.com/css2?family=Lato:wght@400;700&display=swap" rel="stylesheet">
<style>
  :root {
    --backdrop: #3a3330;
    --card: #0e0e0e;
    --blue: #2aa9e3;
    --turquoise: #14b8c0;
    --white: #f2f2f2;
    --silver: #c9c9c9;
    --rule: #3c3c3c;
  }
  * { margin: 0; padding: 0; box-sizing: border-box; }
  html, body {
    width: 1200px; height: 900px; overflow: hidden;
    background: var(--backdrop);
    font-family: "Lato", Arial, sans-serif;
  }
  .spread {
    width: 1200px; height: 900px;
    display: flex; align-items: center; justify-content: center; gap: 50px;
  }
  .card {
    width: 540px; height: 309px;
    background: var(--card);
    position: relative;
    box-shadow: 0 10px 30px rgba(0,0,0,.45);
  }
  /* Contact side */
  .card--contact { display: flex; align-items: center; }
  .brand-block {
    width: 250px; height: 100%;
    display: flex; align-items: center; justify-content: center; gap: 12px;
  }
  .brand-dot {
    width: 22px; height: 22px; border-radius: 50%;
    background: var(--turquoise); flex: none;
  }
  .brand-name {
    color: var(--blue); font-weight: 700; font-size: 22px; line-height: 1.15;
  }
  .divider {
    width: 1px; height: 190px;
    background: linear-gradient(to bottom, transparent, var(--rule) 20%, var(--rule) 80%, transparent);
  }
  .details { padding-left: 26px; color: var(--white); font-size: 15px; line-height: 1.3; }
  .person-name { color: var(--blue); font-weight: 700; font-size: 19px; letter-spacing: .5px; }
  .person-role { margin-bottom: 6px; }
  .contact-line { display: flex; align-items: center; gap: 7px; }
  .contact-line svg { width: 11px; height: 11px; fill: var(--blue); flex: none; }
  .company { color: var(--blue); margin-top: 4px; }
  /* Brand side */
  .card--brand { display: flex; align-items: center; justify-content: center; gap: 14px; }
  .brand-square { width: 26px; height: 26px; background: var(--silver); flex: none; }
  .brand-name--silver { color: var(--silver); font-size: 28px; font-weight: 700; letter-spacing: 1px; }
</style>
</head>
<body>
<main class="spread">
  <section class="card card--contact" aria-label="Contact side">
    <div class="brand-block">
      <span class="brand-dot"></span>
      <span class="brand-name">Corvane<br>Holdings<br>Limited</span>
    </div>
    <div class="divider"></div>
    <div class="details">
      <div class="person-name">MARCUS TELFORD</div>
      <div class="person-role">Director</div>
      <div class="contact-line">
        <svg viewBox="0 0 24 24"><path d="M6.6 10.8a15 15 0 0 0 6.6 6.6l2.2-2.2a1 1 0 0 1 1-.25 11.4 11.4 0 0 0 3.6.57 1 1 0 0 1 1 1V20a1 1 0 0 1-1 1A17 17 0 0 1 3 4a1 1 0 0 1 1-1h3.5a1 1 0 0 1 1 1c0 1.25.2 2.45.57 3.57a1 1 0 0 1-.25 1z"/></svg>
        <span>1 441 732 4590</span>
      </div>
      <div class="contact-line">
        <svg viewBox="0 0 24 24"><path d="M2 5h20v14H2z M2 5l10 8 10-8" /></svg>
        <span>mtelford@corvane.bm</span>
      </div>
      <div class="contact-line">
        <svg viewBox="0 0 24 24"><circle cx="12" cy="12" r="10"/></svg>
        <span>www.corvane.bm</span>
      </div>
      <div class="company">CORVANE HOLDINGS LIMITED</div>
      <div>P.O. Box KR318</div>
      <div>Pemberly KR LT Bermuda</div>
    </div>
  </section>

  <section class="card card--brand" aria-label="Brand side">
    <span class="brand-square"></span>
    <span class="brand-name--silver">CORVANE HOLDINGS</span>
  </section>
</main>
</body>
</html>
```